Design Box Packaging with Logo for a high-end menswear store

I would like to come up with a design for our shipping boxes.
- Printing would only be in 1 colour. (box will be in mid beige/brown)
- I want it to look modern and clean
- I have attached my logo
- It is for a high-end menswear store for shipping clothing for online purchases
Size of the box is about 14 x 10 x 5

Target Market(s)

High-end / wealthy people shopping online

Industry/Entity Type

Clothing, retail, online high-end clothing

Colors

Designer to choose colors to be used in the design.

Requirements
Must have
• Look sharp and clean, have logo information, online printing one colour
Nice to have
• Look clean and modern

```html
<!DOCTYPE html>
<html lang="en">
<head>
<meta charset="utf-8">
<title>Maison Verlaine — Mailer Box Dieline</title>
<link rel="stylesheet" href="https://fonts.googleapis.com/css2?family=Barlow+Semi+Condensed:wght@700&family=Nunito+Sans:wght@400;700&family=Kaushan+Script&family=Arimo:wght@700&display=swap">
<style>
  :root {
    --paper: #fdfbfb;
    --kraft: #e2b39d;
    --ink: #332b2a;
    --ink-deep: #292525;
    --cut: #5a3e35;
    --heading: #000000;
  }
  html, body {
    margin: 0;
    padding: 0;
    width: 1200px;
    height: 720px;
    overflow: hidden;
    background: var(--paper);
  }
  .dieline-sheet { display: block; width: 1200px; height: 720px; }
  .sheet-title { font-family: "Arimo", Arial, sans-serif; font-weight: 700; font-size: 19px; fill: var(--heading); text-anchor: middle; }
  .panel { fill: var(--kraft); stroke: var(--cut); stroke-width: 0.5; }
  .panel-dark { fill: var(--ink); stroke: var(--kraft); stroke-width: 0.4; }
  .slot { fill: none; stroke: var(--cut); stroke-width: 0.5; }
  .tab { fill: var(--ink); }
  .tuck-line { fill: none; stroke: var(--cut); stroke-width: 0.5; }
  .lid-slogan { font-family: "Barlow Semi Condensed", sans-serif; font-weight: 700; font-size: 11px; fill: var(--ink); text-anchor: middle; letter-spacing: 0.3px; }
  .brand-block { fill: var(--ink); }
  .brand-strip { fill: var(--ink-deep); }
  .brand-name { font-family: "Nunito Sans", sans-serif; font-weight: 700; fill: var(--kraft); text-anchor: middle; letter-spacing: 0.4px; }
  .label-corner { fill: none; stroke: var(--ink); stroke-width: 0.7; }
  .label-text { font-family: "Arimo", Arial, sans-serif; font-weight: 700; font-size: 6.6px; fill: var(--ink); text-anchor: middle; }
  .thanks-script { font-family: "Kaushan Script", cursive; font-size: 24px; fill: var(--ink); text-anchor: middle; }
  .note { font-family: "Nunito Sans", sans-serif; fill: var(--ink); text-anchor: middle; }
  .note-small { font-size: 5.4px; }
  .note-body { font-size: 4.4px; }
  .note-mid { font-size: 6.4px; }
  .note-strong { font-size: 6.4px; font-weight: 700; }
</style>
</head>
<body>
<svg class="dieline-sheet" viewBox="0 0 1200 720" xmlns="http://www.w3.org/2000/svg">

  <!-- ===== Outside face ===== -->
  <g class="outside-face">
    <text class="sheet-title" x="358" y="84">Outside part</text>

    <!-- top lid with thumb notch -->
    <path class="panel" d="M239 107 H347 A11 11 0 0 0 369 107 H477 V192 H239 Z"/>
    <polygon class="panel" points="239,107 181,116 181,183 239,192"/>
    <polygon class="panel" points="477,107 534,116 534,183 477,192"/>
    <text class="lid-slogan" x="358" y="154">STEP INTO SPRING WITH STYLE</text>

    <!-- base -->
    <rect class="panel" x="239" y="192" width="238" height="169"/>
    <rect class="slot" x="239" y="215" width="4" height="21"/>
    <rect class="slot" x="239" y="317" width="4" height="21"/>
    <rect class="slot" x="473" y="215" width="4" height="21"/>
    <rect class="slot" x="473" y="317" width="4" height="21"/>

    <!-- left wall -->
    <rect class="panel-dark" x="74" y="196" width="80" height="162"/>
    <rect class="panel-dark" x="154" y="192" width="85" height="169"/>
    <rect class="brand-block" x="175" y="253" width="47" height="47" fill="var(--kraft)" style="fill:var(--kraft)"/>
    <g transform="translate(198.5 276.5) rotate(-90)">
      <text class="brand-name" x="0" y="-2" font-size="7" style="fill:var(--ink)">MAISON</text>
      <text class="brand-name" x="0" y="7" font-size="7" style="fill:var(--ink)">VERLAINE</text>
    </g>

    <!-- right wall -->
    <rect class="panel-dark" x="477" y="192" width="84" height="169"/>
    <rect class="panel-dark" x="561" y="196" width="81" height="162"/>
    <rect class="tab" x="642" y="217" width="3" height="18"/>
    <rect class="tab" x="642" y="318" width="3" height="19"/>
    <rect x="494" y="253" width="46" height="47" style="fill:var(--kraft)"/>
    <g transform="translate(517 276.5) rotate(90)">
      <text class="brand-name" x="0" y="-2" font-size="7" style="fill:var(--ink)">MAISON</text>
      <text class="brand-name" x="0" y="7" font-size="7" style="fill:var(--ink)">VERLAINE</text>
    </g>

    <!-- front wall -->
    <rect class="panel" x="239" y="361" width="238" height="85"/>
    <polygon class="panel" points="239,361 181,371 181,438 239,446"/>
    <polygon class="panel" points="477,361 534,371 534,438 477,446"/>

    <!-- back wall / label panel -->
    <path class="panel" d="M239 446 H477 V632 A16 16 0 0 1 461 648 H255 A16 16 0 0 1 239 632 Z"/>
    <path class="tuck-line" d="M239 617 H257 V614 H459 V617 H477"/>
    <rect class="brand-strip" x="279" y="446" width="46" height="98"/>
    <rect class="brand-strip" x="279" y="553" width="46" height="46"/>
    <text class="brand-name" x="302" y="574" font-size="6.6">MAISON</text>
    <text class="brand-name" x="302" y="583" font-size="6.6">VERLAINE</text>

    <path class="label-corner" d="M358 482 V466 H374"/>
    <path class="label-corner" d="M428 466 H444 V482"/>
    <path class="label-corner" d="M358 581 V597 H374"/>
    <path class="label-corner" d="M428 597 H444 V581"/>
    <text class="label-text" x="401" y="534">SHIPPING LABEL</text>
  </g>

  <!-- ===== Inside face ===== -->
  <g class="inside-face">
    <text class="sheet-title" x="839" y="84">Inside part</text>

    <!-- lid interior -->
    <path class="panel" d="M736 107 H942 A16 16 0 0 1 958 123 V309 H720 V123 A16 16 0 0 1 736 107 Z"/>
    <path class="tuck-line" d="M720 139 H738 V142 H940 V139 H958"/>

    <text class="thanks-script" x="839" y="170">Thank you</text>
    <text class="note note-small" x="839" y="179">FOR SHOPPING WITH US</text>
    <rect class="brand-block" x="821" y="190" width="37" height="36"/>
    <text class="brand-name" x="839.5" y="206" font-size="5.4">MAISON</text>
    <text class="brand-name" x="839.5" y="213" font-size="5.4">VERLAINE</text>

    <text class="note note-body" x="839" y="238">Lorem ipsum dolor sit amet, consectetuer adipiscing elit. Maecenas porttitor</text>
    <text class="note note-body" x="839" y="244.5">congue massa. Fusce posuere, magna sed pulvinar ultricies, purus lectus</text>
    <text class="note note-body" x="839" y="251">malesuada libero, sit amet commodo magna eros quis urna.</text>
    <text class="note note-mid" x="839" y="263">SHARE IT &amp; TAG US !</text>
    <text class="note note-strong" x="839" y="274">@MAISONVERLAINE</text>
    <text class="note note-mid" x="839" y="285">WE HOPE YOU LOVE IT JUST AS MUCH AS WE DO</text>
    <text class="note note-strong" x="839" y="297">www.maisonverlaine.com</text>

    <!-- back wall interior -->
    <rect class="panel" x="720" y="309" width="238" height="84"/>
    <polygon class="panel" points="720,309 663,318 663,385 720,393"/>
    <polygon class="panel" points="958,309 1016,318 1016,385 958,393"/>

    <!-- base interior -->
    <rect class="panel" x="720" y="393" width="238" height="170"/>
    <rect class="slot" x="720" y="416" width="4" height="21"/>
    <rect class="slot" x="720" y="518" width="4" height="21"/>
    <rect class="slot" x="954" y="416" width="4" height="21"/>
    <rect class="slot" x="954" y="518" width="4" height="21"/>

    <rect class="panel-dark" x="555" y="398" width="80" height="161"/>
    <rect class="panel-dark" x="635" y="393" width="85" height="170"/>
    <rect class="panel-dark" x="958" y="393" width="85" height="170"/>
    <rect class="panel-dark" x="1043" y="398" width="81" height="161"/>

    <!-- front wall interior with thumb notch -->
    <path class="panel" d="M720 563 H958 V648 H850 A11 11 0 0 0 828 648 H720 Z"/>
    <polygon class="panel" points="720,563 663,572 663,640 720,648"/>
    <polygon class="panel" points="958,563 1016,572 1016,640 958,648"/>
  </g>
</svg>
</body>
</html>
```